BrivoPeak Business Card Design Project

We are looking for a modern, clean business card design for our new company. We are a consulting firm focused on the financial services market providing management and IT consulting to banks, insurance companies, etc. Please include our company logo and company contact information from the attached file in the design. Two versions of the logo are attached, either version is acceptable. Logos are available in other file formats if needed. We would like to include the contact information for both our UK and US offices as well as the following information for each individual card holder: Name, position/title, address, phone number and e-mail address.
Updates
Project Deadline Extended
Reason: A last minute trip over seas has prevented us from finalizing the decision. A decision will be made this week. We apologize for the inconvenience.
Industry/Entity Type
Business
Contact Information for Business Card
Company logo.
Company locations and phone numbers for both the US and UK offices.
Company URL.
Cardholder Name
Cardholder Position/title
Cardholder Address
Cardholder Phone Number
Cardholder e-mail Address
Look and feel
Each slider illustrates characteristics of the customer's brand and the style your logo design should communicate.

```html
<!DOCTYPE html>
<html lang="en">
<head>
<meta charset="utf-8">
<title>BrivoPeak Partners – Business Card</title>
<link href="https://fonts.googleapis.com/css2?family=Open+Sans:wght@400;600;700&display=swap" rel="stylesheet">
<style>
  :root {
    --navy: #13294f;
    --grey-band: #646464;
    --text-grey: #4a4a4a;
    --rule: #7a7a7a;
    --card: #ffffff;
    --backdrop: #e7e5e2;
  }
  * { margin: 0; padding: 0; box-sizing: border-box; }
  html, body { width: 1200px; height: 1000px; overflow: hidden; }
  body {
    background: var(--backdrop);
    font-family: "Open Sans", Arial, sans-serif;
    color: var(--text-grey);
    position: relative;
  }
  .card {
    position: absolute;
    left: 265px;
    width: 665px;
    height: 397px;
    background: var(--card);
    box-shadow: 0 3px 10px rgba(0,0,0,0.18);
    overflow: hidden;
  }
  .card--front { top: 73px; }
  .card--back { top: 532px; }

  .brand {
    position: absolute;
    display: flex;
    align-items: center;
    gap: 12px;
    font-weight: 700;
    color: var(--navy);
    white-space: nowrap;
  }
  .brand__name { display: block; line-height: 1.1; }
  .brand__mark { background: var(--navy); display: block; flex: none; }
  .card--front .brand { left: 33px; top: 98px; font-size: 38px; }
  .card--front .brand__mark { width: 24px; height: 24px; }
  .card--back .brand { left: 348px; top: 172px; font-size: 42px; }
  .card--back .brand__mark { width: 26px; height: 26px; }

  .holder__name {
    position: absolute;
    right: 32px; top: 209px;
    font-size: 22px; font-weight: 600; color: var(--navy);
    line-height: 28px;
    white-space: nowrap;
  }
  .holder__title {
    position: absolute;
    right: 32px; top: 237px;
    font-size: 14.5px; line-height: 20px;
    white-space: nowrap;
  }
  .holder-rule {
    position: absolute;
    left: 33px; top: 246px;
    width: 480px; height: 1px;
    background: var(--rule);
  }
  .holder-tab {
    position: absolute;
    right: 0; top: 213px;
    width: 9px; height: 41px;
    background: var(--navy);
  }

  .contact-list {
    position: absolute;
    left: 33px; top: 274px;
    list-style: none;
    font-size: 16px;
  }
  .contact-list li {
    display: flex; align-items: center; gap: 8px;
    height: 26px;
  }
  .contact-list svg { width: 15px; height: 15px; fill: var(--navy); flex: none; }

  .bottom-bands { position: absolute; left: 0; bottom: 0; width: 665px; height: 33px; }

  .office {
    position: absolute;
    left: 33px;
    font-size: 16px;
    line-height: 20px;
  }
  .office--us { top: 57px; }
  .office--uk { top: 223px; left: 35px; }
  .office__country { font-size: 17px; font-weight: 700; color: var(--navy); margin-bottom: 8px; }
  .office__phone { display: flex; align-items: center; gap: 6px; margin-top: 7px; }
  .office__phone svg { width: 15px; height: 15px; fill: var(--text-grey); }

  .site-url {
    position: absolute;
    left: 347px; top: 302px;
    font-size: 15px;
    letter-spacing: 2.4px;
    color: var(--text-grey);
    white-space: nowrap;
  }
</style>
</head>
<body>

<section class="card card--front" aria-label="Card front">
  <div class="brand"><span class="brand__mark"></span><span class="brand__name">BrivoPeak<br>Partners</span></div>

  <div class="holder__name">Dalia R. Venner</div>
  <div class="holder__title">Office Manager</div>
  <div class="holder-rule"></div>
  <div class="holder-tab"></div>

  <ul class="contact-list">
    <li>
      <svg viewBox="0 0 16 16" aria-hidden="true"><rect x="4" y="1" width="8" height="14" rx="1.5"/><rect x="5.5" y="3" width="5" height="5" fill="#fff"/></svg>
      + 000 000 0000
    </li>
    <li>
      <svg viewBox="0 0 16 16" aria-hidden="true"><rect x="1" y="3.5" width="14" height="9"/><path d="M1 3.5 L8 9 L15 3.5" stroke="#fff" stroke-width="1.3" fill="none"/></svg>
      info@brivopeakpartners.com
    </li>
    <li>
      <svg viewBox="0 0 16 16" aria-hidden="true"><circle cx="8" cy="8" r="7"/><path d="M1 8 H15 M8 1 C4 5 4 11 8 15 M8 1 C12 5 12 11 8 15" stroke="#fff" stroke-width="1.1" fill="none"/></svg>
      www.brivopeakpartners.com
    </li>
  </ul>

  <svg class="bottom-bands" viewBox="0 0 665 33" aria-hidden="true">
    <polygon points="0,0 318,0 302,33 0,33" fill="var(--grey-band)"/>
    <polygon points="323,3 665,3 665,33 309,33" fill="var(--navy)"/>
  </svg>
</section>

<section class="card card--back" aria-label="Card back">
  <div class="office office--us">
    <div class="office__country">United States</div>
    418 N Harlow Ave,<br>
    Suite 204-117<br>
    Bramford UT 84520
    <div class="office__phone">
      <svg viewBox="0 0 16 16" aria-hidden="true"><path d="M2 6 C2 3 14 3 14 6 L11.5 7 L11 5.5 C9 5 7 5 5 5.5 L4.5 7 Z"/><path d="M4 8 H12 L13 13 H3 Z"/></svg>
      (555) 014-2873
    </div>
  </div>

  <div class="office office--uk">
    <div class="office__country">Great Britain</div>
    14-16 Kestrel Lane<br>
    Ashbury<br>
    AB3 9QX
    <div class="office__phone">
      <svg viewBox="0 0 16 16" aria-hidden="true"><path d="M2 6 C2 3 14 3 14 6 L11.5 7 L11 5.5 C9 5 7 5 5 5.5 L4.5 7 Z"/><path d="M4 8 H12 L13 13 H3 Z"/></svg>
      +44 7700 900418
    </div>
  </div>

  <div class="brand"><span class="brand__mark"></span><span class="brand__name">BrivoPeak<br>Partners</span></div>
  <div class="site-url">www.brivopeakpartners.com</div>
</section>

</body>
</html>
```